Business card for massage therapy company called Brook Fern Wellness

Need business card for massage therapy company called Brook Fern Wellness. Would like my logo on the front and the back of the card I have 3 options of logos and you can play with what looks better.

Would like this information displayed on the back of the card:

Marcus Ellery
Licensed Massage Therapist
321-555-0147
brookfern-example.com
brookfern_rest_

```html
<!DOCTYPE html>
<html lang="en">
<head>
<meta charset="utf-8">
<title>Brook Fern Wellness – Business Card</title>
<link href="https://fonts.googleapis.com/css2?family=Montserrat:wght@300;400;500;600&display=swap" rel="stylesheet">
<style>
  :root {
    --sage: #757b62;
    --sage-dark: #5f6650;
    --clay: #c39a78;
    --paper: #ffffff;
    --backdrop: #3a3a3a;
    --ink-light: #f4f2ec;
  }
  * { box-sizing: border-box; margin: 0; padding: 0; }
  html, body {
    width: 1200px; height: 875px; overflow: hidden;
    background: var(--backdrop);
    font-family: "Montserrat", sans-serif;
  }
  .canvas { position: relative; width: 1200px; height: 875px; }

  .card {
    position: absolute; left: 280px;
    width: 640px; height: 366px;
    border-radius: 22px; overflow: hidden;
  }

  /* Wordmark: one colour, one weight; second line set smaller and wider */
  .wordmark {
    font-weight: 400; text-transform: uppercase; line-height: 1;
    display: flex; flex-direction: column;
  }
  .wordmark .primary { letter-spacing: 0.2em; }
  .wordmark .secondary { font-size: 0.56em; letter-spacing: 0.62em; margin-top: 0.35em; }

  /* Front */
  .card--front { top: 48px; background: var(--sage); }
  .front-mark {
    position: absolute; inset: 0;
    display: flex; flex-direction: column; align-items: center; justify-content: center; gap: 22px;
  }
  .mark-circle {
    width: 96px; height: 96px; border-radius: 50%;
    border: 2px solid var(--ink-light);
  }
  .card--front .wordmark { color: var(--ink-light); font-size: 32px; align-items: center; text-align: center; }
  .card--front .wordmark .secondary { padding-left: 0.62em; }

  /* Back */
  .card--back { top: 461px; background: var(--paper); }
  .card--back svg.shapes { position: absolute; inset: 0; }
  .back-wordmark {
    position: absolute; left: 40px; top: 50px;
    color: var(--sage-dark); font-size: 28px; align-items: flex-start;
  }
  .back-wordmark .secondary { margin-left: 1.6em; }
  .identity { position: absolute; left: 40px; top: 186px; }
  .identity .name {
    color: var(--clay); font-weight: 600; font-size: 21px;
    letter-spacing: 0.02em; text-transform: uppercase;
  }
  .identity .role { color: var(--ink-light); font-size: 12.5px; font-weight: 400; margin-top: 2px; }
  .identity .rule { width: 14px; height: 1px; background: var(--clay); margin: 10px 0 8px; }
  .contact { list-style: none; }
  .contact li {
    display: flex; align-items: center; gap: 8px;
    color: var(--ink-light); font-size: 11.5px; line-height: 19px;
  }
  .contact .icon { width: 12px; height: 12px; flex: none; }
</style>
</head>
<body>
<div class="canvas">

  <section class="card card--front" aria-label="Card front">
    <div class="front-mark">
      <div class="mark-circle"></div>
      <p class="wordmark"><span class="primary">Brook Fern</span><span class="secondary">Wellness</span></p>
    </div>
  </section>

  <section class="card card--back" aria-label="Card back">
    <svg class="shapes" width="640" height="366" viewBox="0 0 640 366">
      <polygon points="455,40 640,40 640,300 520,300" fill="var(--clay)"/>
      <polygon points="0,172 430,100 560,330 0,330" fill="var(--sage)"/>
      <circle cx="500" cy="190" r="108" fill="var(--paper)"/>
      <circle cx="500" cy="190" r="96" fill="none" stroke="var(--sage)" stroke-width="3"/>
    </svg>

    <p class="wordmark back-wordmark"><span class="primary">Brook Fern</span><span class="secondary">Wellness</span></p>

    <div class="identity">
      <p class="name">Marcus Ellery</p>
      <p class="role">Licensed Massage Therapist</p>
      <div class="rule"></div>
      <ul class="contact">
        <li>
          <svg class="icon" viewBox="0 0 12 12"><path d="M3 1 L5 3.5 L4 5 Q5 7 7 8 L8.5 7 L11 9 L10 11 Q4 11 1 2 Z" fill="var(--clay)"/></svg>
          321-555-0147
        </li>
        <li>
          <svg class="icon" viewBox="0 0 12 12"><rect x="1" y="2.5" width="10" height="7" fill="var(--clay)"/><path d="M1 2.5 L6 6.5 L11 2.5" fill="none" stroke="var(--sage)" stroke-width="1"/></svg>
          info@brookfern-example.com
        </li>
        <li>
          <svg class="icon" viewBox="0 0 12 12"><circle cx="6" cy="6" r="5" fill="none" stroke="var(--clay)" stroke-width="1.2"/><ellipse cx="6" cy="6" rx="2" ry="5" fill="none" stroke="var(--clay)"/><line x1="1" y1="6" x2="11" y2="6" stroke="var(--clay)"/></svg>
          www.brookfern-example.com
        </li>
        <li>
          <svg class="icon" viewBox="0 0 12 12"><line x1="3" y1="6" x2="9" y2="2.5" stroke="var(--clay)" stroke-width="1.1"/><line x1="3" y1="6" x2="9" y2="9.5" stroke="var(--clay)" stroke-width="1.1"/><circle cx="3" cy="6" r="2" fill="var(--clay)"/><circle cx="9" cy="2.5" r="2" fill="var(--clay)"/><circle cx="9" cy="9.5" r="2" fill="var(--clay)"/></svg>
          @brookfern_rest_
        </li>
      </ul>
    </div>
  </section>

</div>
</body>
</html>
```